Mortgage Protection Insurance Flyer

The target audience are new home owners so the design needs to be clean and simple.

This a primarily for Final Expense Insurance, but need an area where it says "We Also Specialize In:"
- Medicare Supplement Insurance (MediGap)
- Annuities
- Final Expense

All flyer versions need to be editable. Colors to be used are red, white or black. Refer to my website for colors and photos (brightmeadowcover.com). Will attach my logo and a flyer that I found online that is the format that I am looking for (for 8.5 in. x 11 in version). Need flyer in standard letter size 8.5 in. x11 in. but also in 8.5 in. x 5.5 in and 5.0 in. x 8.0 in. All sizes to be portrait oriented. If picked as winning design, need all flyer versions in full color, also in grey scale and files in all industry file types.

Content can be taken from my website..... brightmeadowcover.com

Do NOT submit if you are not willing to provide all versions as described above for the original project price.

Must use royalty-free stock photos please.

Target Market(s)

New homeowners looking for insurance to protect there mortgage payments

Industry/Entity Type

Life Insurance

Colors
f69fa3

Requirements
Must have
• Colors to be used are red, white or black.
• Need flyer in standard letter size 8.5 in. x11 in. but also in 3.5 in. x 8.5 in (Full Bleed 3.75 in by 8.75 in.) and 4.0 in. x 6.0 in. (Full Bleed 4.12 in x 6.12 in) Each design tailored to the size dimensions (So no squeezing 8.5 x 11 design into a 4.0 x 6.0 space.) All sizes to be portrait oriented. If picked as winning design, need all flyer versions in full color, also in grey scale and files in all file types.
• Do not need physical address on flyer, do need email address on flyer though - tkelvin@brightmeadowcover.com
• So phone number should be prominent, email address and website address should also be contact area.
• If you can not agree to terms above, do not submit any designs.
• Need facebook & twitter logos somewhere in contact info area.
Nice to have
• See sample flyers I have attached.
• White background with red used as primary graphic color and black used as secondary graphic if needed.
• font to be used should similar to one used in logo.

```html
<!DOCTYPE html>
<html lang="en">
<head>
<meta charset="utf-8">
<title>Brightmeadow Cover – Mortgage Protection Flyer</title>
<link href="https://fonts.googleapis.com/css2?family=Exo+2:ital,wght@1,900&family=Montserrat:wght@400;500;600;700;800&display=swap" rel="stylesheet">
<style>
  :root {
    --red: #e0262f;
    --red-light: #e8434b;
    --ink: #2b2b2b;
    --text: #444444;
    --paper: #ececec;
    --grey-bar: #4a4a4a;
    --footer-dark: #262626;
    --stage: #3b3b3b;
    --white: #ffffff;
  }
  * { box-sizing: border-box; margin: 0; padding: 0; }
  html, body { width: 1200px; height: 857px; overflow: hidden; }
  body {
    background: var(--stage);
    font-family: "Montserrat", Arial, sans-serif;
    color: var(--text);
    position: relative;
  }
  .flyer {
    position: absolute;
    left: 294px; top: 18px;
    width: 612px; height: 820px;
    background: var(--paper);
    overflow: hidden;
  }
  .hero {
    position: absolute; left: 0; top: 0; width: 612px; height: 320px;
    background: linear-gradient(90deg, #f1f1f1 0%, #e9e9e9 55%, #dcdcdc 100%);
  }
  .hero-photo {
    position: absolute; right: 0; top: 0; width: 300px; height: 320px;
    background: linear-gradient(160deg, #f2f2f2 0%, #d6d3d0 40%, #b8b2ad 70%, #8f95a3 100%);
  }
  .brand {
    position: absolute; left: 29px; top: 76px;
    display: flex; align-items: center; gap: 7px;
    font-weight: 800; font-size: 19px; letter-spacing: .3px;
    color: var(--ink); text-transform: uppercase; white-space: nowrap;
  }
  .brand-dot { width: 11px; height: 11px; border-radius: 50%; background: var(--red); }
  .promo {
    position: absolute; left: 0; top: 139px; width: 294px; height: 144px;
    background: linear-gradient(90deg, var(--red-light), var(--red));
    padding: 16px 14px 0 28px; color: var(--white);
  }
  .promo-title {
    font-family: "Exo 2", Arial, sans-serif; font-style: italic; font-weight: 900;
    font-size: 21.5px; line-height: 25px; text-transform: uppercase;
  }
  .promo-text { margin-top: 9px; font-size: 11.2px; line-height: 15px; font-weight: 500; text-align: left; }
  .col-left { position: absolute; left: 28px; top: 345px; width: 266px; }
  .col-right { position: absolute; left: 324px; top: 345px; width: 258px; }
  .section-title { color: var(--red); font-weight: 700; font-size: 12px; margin-bottom: 7px; }
  .about-title {
    font-family: "Exo 2", Arial, sans-serif; font-style: italic; font-weight: 900;
    color: var(--red); font-size: 15.5px; margin-bottom: 8px;
  }
  .sub-title { color: var(--ink); font-weight: 600; font-size: 12.2px; margin-bottom: 4px; }
  .sub-title.gap { margin-top: 15px; }
  p { font-size: 9.9px; line-height: 12.4px; text-align: justify; }
  .gap { margin-top: 20px; }
  .also-title { margin-top: 6px; font-size: 9.9px; font-weight: 600; color: var(--ink); }
  .ticks { list-style: none; margin-top: 4px; }
  .ticks li {
    position: relative; padding-left: 13px; font-size: 9.9px; line-height: 12.4px;
    margin-bottom: 6.3px; text-align: justify;
  }
  .ticks.tight li { margin-bottom: 3.5px; font-size: 9.3px; }
  .ticks svg { position: absolute; left: 0; top: 2px; width: 8px; height: 8px; }
  .rates { margin-top: 24px; }
  .rate-row { display: flex; gap: 2px; margin-bottom: 3px; height: 20px; }
  .rate-label {
    flex: 0 0 172px; background: var(--grey-bar); color: var(--white);
    font-size: 9.9px; padding-left: 11px; display: flex; align-items: center;
  }
  .rate-value {
    flex: 1; background: var(--red); color: var(--white); font-size: 10px; font-weight: 500;
    display: flex; align-items: center; justify-content: center;
  }
  .rate-note { margin-top: 22px; color: var(--ink); font-size: 10.2px; line-height: 12.4px; }
  .footer { position: absolute; left: 0; top: 768px; width: 612px; height: 52px; }
  .footer svg.band { position: absolute; left: 0; top: 0; }
  .phone {
    position: absolute; left: 28px; top: 11px; display: flex; align-items: center; gap: 7px;
    color: var(--white); font-weight: 700; font-size: 18.5px;
  }
  .contact {
    position: absolute; left: 220px; top: 16px; display: flex; align-items: center; gap: 9px;
    color: var(--white); font-size: 9.4px; white-space: nowrap;
  }
  .contact span { display: flex; align-items: center; gap: 4px; }
  .social { display: flex; gap: 4px; }
  .social-dot { width: 11px; height: 11px; border-radius: 50%; background: var(--red); }
</style>
</head>
<body>
<main class="flyer">
  <section class="hero">
    <div class="hero-photo" role="img" aria-label="Photo of a smiling couple embracing in their bright new home"></div>
    <div class="brand"><span class="brand-dot"></span>Brightmeadow Cover</div>
    <div class="promo">
      <h1 class="promo-title">Our plans are based<br>on yours</h1>
      <p class="promo-text">New homeowner? Get the right Mortgage Protection, Final Expense or Medicare Supplement plan to protect your home and your family's peace-of-mind!</p>
    </div>
  </section>

  <section class="col-left">
    <h2 class="section-title">Final Expense Insurance</h2>
    <p>Final Expense Insurance is a type of permanent life insurance where the death benefit is used to cover (but not limited to) medical costs, funeral costs and other end-of-life expenses. It is a budget friendly option with a death benefit of up to $40k.</p>
    <h2 class="section-title gap" style="margin-bottom:2px">Benefits:</h2>
    <ul class="ticks">
      <li><svg viewBox="0 0 10 10"><rect x="1" y="1" width="8" height="8" fill="none" stroke="#e0262f" stroke-width="1.4"/><path d="M2.5 5l2 2 4.5-5" fill="none" stroke="#e0262f" stroke-width="1.5"/></svg>All plans we offer are state regulated</li>
      <li><svg viewBox="0 0 10 10"><rect x="1" y="1" width="8" height="8" fill="none" stroke="#e0262f" stroke-width="1.4"/><path d="M2.5 5l2 2 4.5-5" fill="none" stroke="#e0262f" stroke-width="1.5"/></svg>Relatively low monthly premiums</li>
      <li><svg viewBox="0 0 10 10"><rect x="1" y="1" width="8" height="8" fill="none" stroke="#e0262f" stroke-width="1.4"/><path d="M2.5 5l2 2 4.5-5" fill="none" stroke="#e0262f" stroke-width="1.5"/></svg>Premiums can never increase</li>
      <li><svg viewBox="0 0 10 10"><rect x="1" y="1" width="8" height="8" fill="none" stroke="#e0262f" stroke-width="1.4"/><path d="M2.5 5l2 2 4.5-5" fill="none" stroke="#e0262f" stroke-width="1.5"/></svg>Your policy can never be cancelled as long as you pay your premium</li>
      <li><svg viewBox="0 0 10 10"><rect x="1" y="1" width="8" height="8" fill="none" stroke="#e0262f" stroke-width="1.4"/><path d="M2.5 5l2 2 4.5-5" fill="none" stroke="#e0262f" stroke-width="1.5"/></svg>No medical exams</li>
      <li><svg viewBox="0 0 10 10"><rect x="1" y="1" width="8" height="8" fill="none" stroke="#e0262f" stroke-width="1.4"/><path d="M2.5 5l2 2 4.5-5" fill="none" stroke="#e0262f" stroke-width="1.5"/></svg>Guaranteed Death Benefit</li>
      <li><svg viewBox="0 0 10 10"><rect x="1" y="1" width="8" height="8" fill="none" stroke="#e0262f" stroke-width="1.4"/><path d="M2.5 5l2 2 4.5-5" fill="none" stroke="#e0262f" stroke-width="1.5"/></svg>Many policies we offer are Guaranteed Acceptance, "Day 1" coverage, have a child/grandchild rider and/or have an accelerated death benefit rider</li>
    </ul>
    <div class="rates">
      <div class="rate-row"><div class="rate-label">Monthly premiums as low as</div><div class="rate-value">$10</div></div>
      <div class="rate-row"><div class="rate-label">Death Benefits as high as</div><div class="rate-value">$40,000</div></div>
    </div>
    <p class="rate-note">Based on an insured that is a 65 year old, non-smoking female that has no medical conditions with death benefit of $2k</p>
  </section>

  <section class="col-right">
    <h2 class="about-title">ABOUT US</h2>
    <h3 class="sub-title">We Work for You</h3>
    <p style="text-align:left">We help new homeowners in North Idaho/<br>Eastern Washington protect their mortgage<br>and prepare for the unknown.</p>
    <p class="also-title">We Also Specialize In:</p>
    <ul class="ticks tight" style="margin-top:4px">
      <li><svg viewBox="0 0 10 10"><rect x="1" y="1" width="8" height="8" fill="none" stroke="#e0262f" stroke-width="1.4"/><path d="M2.5 5l2 2 4.5-5" fill="none" stroke="#e0262f" stroke-width="1.5"/></svg>Medicare Supplement Insurance (MediGap)</li>
      <li><svg viewBox="0 0 10 10"><rect x="1" y="1" width="8" height="8" fill="none" stroke="#e0262f" stroke-width="1.4"/><path d="M2.5 5l2 2 4.5-5" fill="none" stroke="#e0262f" stroke-width="1.5"/></svg>Annuities</li>
      <li><svg viewBox="0 0 10 10"><rect x="1" y="1" width="8" height="8" fill="none" stroke="#e0262f" stroke-width="1.4"/><path d="M2.5 5l2 2 4.5-5" fill="none" stroke="#e0262f" stroke-width="1.5"/></svg>Final Expense</li>
    </ul>
    <p style="margin-top:4px">We have access to the industry's top insurance carriers so you can get the right coverage that fits your budget.</p>
    <h3 class="sub-title gap">Assessing Need</h3>
    <p>Unforeseen events and a lack of the right kind of insurance can spell trouble quickly. Contact us today, to set up a free assessment time. We will analyze your insurance needs and get you and your family the right coverage quickly at a budget friendly price.</p>
    <h3 class="sub-title gap">Your Unique</h3>
    <p style="text-align:left">Everyone has different insurance needs.</p>
    <p>Find out how we can give you the peace of mind knowing your family wont lose their home if something were to happen to you.</p>
    <p>and/or</p>
    <p>Find out how we can help find the right plan to keep your medical costs manageable.</p>
  </section>

  <footer class="footer">
    <svg class="band" width="612" height="52" viewBox="0 0 612 52">
      <rect width="612" height="52" fill="#262626"/>
      <polygon points="0,0 197,0 215,46 612,46 612,52 0,52" fill="#e0262f"/>
    </svg>
    <div class="phone">
      <svg width="20" height="20" viewBox="0 0 24 24"><path d="M6.6 10.8a15.2 15.2 0 0 0 6.6 6.6l2.2-2.2c.3-.3.7-.4 1-.2 1.1.4 2.3.6 3.6.6.6 0 1 .4 1 1V20c0 .6-.4 1-1 1A17 17 0 0 1 3 4c0-.6.4-1 1-1h3.5c.6 0 1 .4 1 1 0 1.3.2 2.5.6 3.6.1.3 0 .7-.2 1z" fill="#fff"/></svg>
      (208)555.0147
    </div>
    <div class="contact">
      <span><svg width="9" height="7" viewBox="0 0 10 8"><rect width="10" height="8" rx="1" fill="#e0262f"/><path d="M0.5 1l4.5 3.5L9.5 1" fill="none" stroke="#fff" stroke-width="1"/></svg>tkelvin@brightmeadowcover.com</span>
      <span><svg width="8" height="8" viewBox="0 0 10 10"><circle cx="5" cy="5" r="4.3" fill="none" stroke="#e0262f" stroke-width="1.3"/><path d="M0.7 5h8.6M5 0.7c-2.5 2.6-2.5 6 0 8.6M5 0.7c2.5 2.6 2.5 6 0 8.6" fill="none" stroke="#e0262f" stroke-width="1"/></svg>www.brightmeadowcover.com</span>
      <span class="social">
        <span class="social-dot" role="img" aria-label="Social network profile link"></span>
        <span class="social-dot" role="img" aria-label="Second social network profile link"></span>
      </span>
    </div>
  </footer>
</main>
</body>
</html>
```